Webdesign für vielseitiges Unternehmen
Zielgruppe
Die Seite wird HOCHMOOR-ART oder DESIGN heißen.
Das Unternehmen bietet folgende Segmente an:
1. Möbelstücke (meist Unikate, da restauriert mit eigener Kreation)
2. Fotografien
3. Malerei
4. Interieurdesign (Gestalten, Einrichten von Apartments, Häusern, Shops etc.) (hier muss natürlich mehr Platz für Informationstext sein.
5. Gallery. - Infos zu Öffnungszeiten und Bilder ebenfalls.
6. Die Location ist für Events buchbar
(7.) Blogg wenns nicht zu aufwändig ist. (hier möchte ich gern Bilder posten die ich irgendwo finde und als gut erachte. Oder Produkte. Wichtig ist, dass bei Verbreitung von Fremdpostings, immer die Quelle eingefügt werden muss. Am besten automatisch. Ich muss zu dem Post noch eigenes Kommentar abgeben können.
Für jedes Segment soll eine Unterseite geschaffen werden.
Die Produktfotos sollen clean aufgebaut sein. Am besten je Produkt 1 Bild pro Seite. Vielleicht erst nachdem man auf ein Bild in der Auswahl geklickt hat?? 3 nebeneinander und dann neue Zeile.
Unter den Bildern (hauptsächlich Querformat aber Hochformat muss auch gehen) müssen Angaben stehen:
-Art
-Size
-Auflage
-Preis
-liken für Social Media oder weiterleiten (wenn möglich)
-Fragen zu diesem Produkt ( wenn hier jemand klickt und etwas schreibt, muss ich eine mail erhalten, wo ich direkt ersehen kann, zu welchem Produkt die Frage zugeordnet ist.
Pro Artikel müssen mehrere Bilder eingestellt werden können, die der Client durch einfaches klicken durchklicken kann.
Die Seite soll clean, chic und Edel wirken. Hauptsächlich über Bilder. Shopsystem ist wegen Aufwandskosten erstmal nicht geplant)
Ich muss die Seite selber pflegen können, auch SEO Optimieren (ohne Programierkenntnisse)
Die Seite soll eine Seite für verschiedene Aspekte sein wie:
- Gallerie
hier wird die Gallerie vorgestellt und Bilder gezeigt von Ausstellungen und Künstlervorstellung..
Aufgabenstellung
Schwarz- Weiß
Akzente eventuell in Patinagrün oder Grünspan oder Malachitgrün oder Gold
Mobilgeräte responsiv

```html
<!DOCTYPE html>
<html lang="de">
<head>
<meta charset="utf-8">
<title>HOCHMOOR – Interieur · Design · Galerie</title>
<link href="https://fonts.googleapis.com/css2?family=Source+Sans+3:wght@300;400;600&display=swap" rel="stylesheet">
<style>
  :root {
    --ink: #1c1c1c;
    --paper: #ffffff;
    --gold: #f2cf62;
    --text: #3e3e3e;
    --muted: #8a8a8a;
    --green: #3f6b5c;
    --green-soft: #e1e8e4;
    --line: #c9c9c9;
    --dot: #c4c4c4;
  }
  * { box-sizing: border-box; margin: 0; padding: 0; }
  html, body { width: 1200px; height: 1106px; overflow: hidden; background: var(--paper); }
  body { position: relative; font-family: "Source Sans 3", sans-serif; font-weight: 300; color: var(--text); }

  .site-header { position: absolute; left: 0; top: 0; width: 1200px; height: 112px; background: var(--ink); border-bottom: 4px solid var(--gold); box-shadow: 0 2px 4px rgba(0,0,0,.15); }
  .brand { position: absolute; left: 74px; top: 36px; color: #fff; }
  .brand-name { font-size: 30px; font-weight: 600; letter-spacing: 1px; line-height: 1; }
  .brand-tag { font-size: 8px; font-weight: 600; letter-spacing: 2.4px; margin-top: 3px; padding-left: 22px; }
  .main-nav a { position: absolute; top: 48px; font-size: 17px; color: #fff; text-decoration: none; line-height: 1; }
  .main-nav a.is-active { color: var(--gold); }

  .intro-title { position: absolute; left: 74px; top: 190px; font-size: 37px; font-weight: 400; color: var(--text); }
  .fav-button { position: absolute; left: 74px; top: 271px; width: 150px; height: 38px; border-radius: 4px; background: var(--green-soft); display: flex; align-items: center; gap: 10px; padding-left: 16px; font-size: 18px; font-weight: 400; color: var(--green); }
  .fav-button svg { width: 20px; height: 20px; }

  .intro-copy { position: absolute; left: 74px; top: 354px; width: 450px; font-size: 18px; line-height: 43px; }

  .question-form { position: absolute; left: 77px; top: 758px; width: 430px; }
  .question-form p { font-size: 13px; color: var(--muted); margin-bottom: 10px; }
  .field { height: 38px; border: 2px solid var(--line); border-radius: 6px; font-size: 14px; color: var(--muted); padding: 9px 11px; }
  .field + .field { margin-top: 15px; }
  .field-row { position: relative; margin-top: 15px; }
  .send-button { position: absolute; right: 0; top: 0; width: 60px; height: 38px; background: var(--green); border-radius: 4px; display: flex; align-items: center; justify-content: center; box-shadow: 0 4px 8px rgba(255,120,140,.25); }

  .gallery-stack { position: absolute; }
  .stack-back { left: 1080px; top: 369px; width: 45px; height: 410px; background: linear-gradient(180deg, #dcdcdc, #cfd4d8 50%, #e4e4e4); }
  .stack-mid { left: 1042px; top: 328px; width: 38px; height: 492px; background: linear-gradient(180deg, #b4b4b2, #9a9b99 50%, #b8b8b6); }
  .stack-front { left: 650px; top: 285px; width: 392px; height: 578px; background: linear-gradient(180deg, #f1f0ee 0%, #ece9e4 55%, #b08a62 80%, #9a7450 100%); }

  .slider-dots { position: absolute; top: 946px; left: 0; width: 1200px; }
  .slider-dots span { position: absolute; width: 8px; height: 8px; border-radius: 50%; background: var(--dot); top: 2px; }
  .slider-dots span.is-current { width: 12px; height: 12px; top: 0; background: var(--green); }

  .site-footer { position: absolute; left: 0; top: 993px; width: 1200px; height: 113px; background: var(--ink); box-shadow: 0 -2px 4px rgba(0,0,0,.15); color: #fff; font-size: 17px; text-align: center; padding-top: 50px; padding-left: 32px; }
</style>
</head>
<body>
  <header class="site-header">
    <div class="brand">
      <div class="brand-name">HOCHMOOR</div>
      <div class="brand-tag">INTERIEUR · DESIGN · GALERIE</div>
    </div>
    <nav class="main-nav">
      <a class="is-active" style="left:358px">HOME</a>
      <a style="left:436px">ÜBER UNS</a>
      <a style="left:554px">GALLERIE</a>
      <a style="left:662px">FOTOGRAFIE</a>
      <a style="left:796px">MALEREI</a>
      <a style="left:900px">INTERIEUR</a>
      <a style="left:1022px">BLOG</a>
      <a style="left:1104px">KONTAKT</a>
    </nav>
  </header>

  <h1 class="intro-title">Willkommen bei HOCHMOOR.</h1>

  <div class="fav-button">
    <svg viewBox="0 0 24 24" fill="none" stroke="#1c1c1c" stroke-width="2.2" stroke-linejoin="round"><path d="M12 20.5 4 12.8A4.8 4.8 0 0 1 12 6.4a4.8 4.8 0 0 1 8 6.4Z"/></svg>
    Favoriten
  </div>

  <p class="intro-copy">Lorem ipsum dolor sit amet, consetetur sadipscing elitr, sed diam nonumy eirmod tempor invidunt ut labore et dolore magna aliquyam erat, sed diam voluptua. At vero eos et accusam et justo duo dolores et ea rebum. Stet clita kasd gubergren, no sea takimata sanctus est Lorem ipsum dolor sit amet. Lorem ipsum dolor sit amet, consetetur sadipscing elitr, sed diam nonumy eirmod tempor invidunt ut labore et dolore magna aliquyam erat, sed diam voluptua.</p>

  <form class="question-form">
    <p>Stellen Sie uns eine Frage zu Kunstwerk 123, wir helfen Ihnen gerne weiter.</p>
    <div class="field">Ihre Email</div>
    <div class="field-row">
      <div class="field">Ihre FRage</div>
      <div class="send-button">
        <svg width="24" height="22" viewBox="0 0 24 22" fill="none" stroke="#fff" stroke-width="1.8" stroke-linejoin="round"><path d="M2 2 22 11 2 20 6 11Z M6 11H22"/></svg>
      </div>
    </div>
  </form>

  <div class="gallery-stack stack-back" role="img" aria-label="Weiteres Galeriefoto: heller Ausstellungsraum"></div>
  <div class="gallery-stack stack-mid" role="img" aria-label="Weiteres Galeriefoto: Raum mit Betonwand"></div>
  <div class="gallery-stack stack-front" role="img" aria-label="Foto eines Schlafzimmers mit rundem Spiegel, weißer Kommode, Pflanze und Holzboden"></div>

  <div class="slider-dots">
    <span class="is-current" style="left:557px"></span>
    <span style="left:588px"></span>
    <span style="left:615px"></span>
    <span style="left:642px"></span>
  </div>

  <footer class="site-footer">HOCHMOOR GmbH • Musterstrasse 123, 12345 Musterstadt, Deutschland • T. +00 123 123 1234 &nbsp;• M. info@hochmoor-art.de</footer>
</body>
</html>
```